Venlow Partners
Global Real Estate Investing
Venlow Partners -
Creative Brief
Modern
Ravi Talbert
President
24817 Mobley Lane 2nd Floor Lakeford OH 44090
rtalbert@venlowpartners.example
www.venlowpartners.example

```html
<!DOCTYPE html>
<html lang="en">
<head>
<meta charset="utf-8">
<title>Venlow Partners – Business Card</title>
<link href="https://fonts.googleapis.com/css2?family=Open+Sans:wght@400;600;700;800&display=swap" rel="stylesheet">
<style>
  :root {
    --page-bg: #3a3a3c;
    --card-white: #ffffff;
    --brand-blue: #1f3a9e;
    --swoosh-blue: #2340b8;
    --swoosh-deep: #16288a;
    --swoosh-grey: #6e7587;
    --text-grey: #4a4d55;
    --icon-grey: #3d4150;
  }
  * { box-sizing: border-box; margin: 0; padding: 0; }
  html, body {
    width: 1200px; height: 780px; overflow: hidden;
    background: var(--page-bg);
    font-family: "Open Sans", Arial, sans-serif;
  }
  .business-card {
    position: absolute; left: 80px; top: 93px;
    width: 1040px; height: 594px;
    background: var(--card-white);
    border-radius: 26px;
    overflow: hidden;
  }
  .card-swoosh { position: absolute; inset: 0; }
  .brand {
    position: absolute; left: 62px; top: 100px;
    display: flex; align-items: center; gap: 18px;
  }
  .brand-dot {
    width: 76px; height: 76px; border-radius: 50%;
    background: var(--brand-blue);
  }
  .brand-name {
    font-weight: 800; font-size: 44px; letter-spacing: 1px;
    color: var(--brand-blue); line-height: 1;
  }
  .contact-person {
    position: absolute; left: 80px; top: 262px;
    display: flex; align-items: baseline; gap: 28px;
    color: var(--brand-blue);
  }
  .person-name { font-weight: 700; font-size: 30px; }
  .person-title { font-weight: 600; font-size: 22px; }
  .address {
    position: absolute; left: 80px; top: 316px;
    font-size: 21px; line-height: 30px; color: var(--text-grey);
  }
  .contact-list {
    position: absolute; left: 80px; top: 410px;
    list-style: none; font-size: 20px; color: var(--text-grey);
  }
  .contact-list li { display: flex; align-items: center; height: 40px; gap: 12px; }
  .contact-list svg { width: 22px; height: 22px; fill: var(--icon-grey); flex: none; }
  .phone-pair .gap { width: 16px; }
</style>
</head>
<body>
  <div class="business-card">
    <svg class="card-swoosh" viewBox="0 0 1040 594" aria-hidden="true">
      <defs>
        <linearGradient id="blueSweep" x1="0" y1="0" x2="1" y2="0">
          <stop offset="0" stop-color="#16288a"/>
          <stop offset="1" stop-color="#2340b8"/>
        </linearGradient>
      </defs>
      <path d="M740,0 C900,70 990,260 870,594 L1040,594 L1040,0 Z" fill="url(#blueSweep)"/>
      <path d="M820,594 C900,420 905,280 880,190 C925,300 930,450 870,594 Z" fill="#6e7587"/>
    </svg>

    <div class="brand">
      <span class="brand-dot"></span>
      <span class="brand-name">VENLOW PARTNERS</span>
    </div>

    <div class="contact-person">
      <span class="person-name">Ravi Talbert</span>
      <span class="person-title">President</span>
    </div>

    <p class="address">24817 Mobley Lane 2nd Floor<br>Lakeford OH 44090</p>

    <ul class="contact-list">
      <li class="phone-pair">
        <svg viewBox="0 0 24 24"><path d="M6.6 10.8a15 15 0 0 0 6.6 6.6l2.2-2.2a1 1 0 0 1 1-.25 11.4 11.4 0 0 0 3.6.57 1 1 0 0 1 1 1V20a1 1 0 0 1-1 1A17 17 0 0 1 3 4a1 1 0 0 1 1-1h3.5a1 1 0 0 1 1 1c0 1.25.2 2.450.57 3.6a1 1 0 0 1-.25 1z"/></svg>
        <span>555-014-2790</span>
        <span class="gap"></span>
        <svg viewBox="0 0 24 24"><path d="M6 2h10v6H6zM4 9h16a2 2 0 0 1 2 2v7h-4v4H6v-4H2v-7a2 2 0 0 1 2-2zm4 8v3h8v-3z"/></svg>
        <span>555-014-2790</span>
      </li>
      <li>
        <svg viewBox="0 0 24 24"><path d="M12 2a10 10 0 1 0 5 18.7l-1-1.7A8 8 0 1 1 20 12v1.5a1.5 1.5 0 0 1-3 0V7h-2v1a5 5 0 1 0 .7 6.6A3.5 3.5 0 0 0 22 13.5V12A10 10 0 0 0 12 2zm0 13a3 3 0 1 1 0-6 3 3 0 0 1 0 6z"/></svg>
        <span>rtalbert@venlowpartners.example</span>
      </li>
      <li>
        <svg viewBox="0 0 24 24"><path d="M12 2a10 10 0 1 0 0 20 10 10 0 0 0 0-20zm6.9 6h-3a15 15 0 0 0-1.3-3.9A8 8 0 0 1 18.9 8zM12 4c.8 1.2 1.5 2.5 1.9 4h-3.8c.4-1.5 1.1-2.8 1.9-4zM4.3 14a8 8 0 0 1 0-4h3.4a16 16 0 0 0 0 4zm.8 2h3a15 15 0 0 0 1.3 3.9A8 8 0 0 1 5.1 16zm3-8h-3a8 8 0 0 1 4.3-3.9A15 15 0 0 0 8.1 8zM12 20c-.8-1.2-1.5-2.5-1.9-4h3.8c-.4 1.5-1.1 2.8-1.900 4zm2.3-6H9.7a14 14 0 0 1 0-4h4.6a14 14 0 0 1 0 4zm.3 5.9a15 15 0 0 0 1.3-3.9h3a8 8 0 0 1-4.3 3.9zm1.7-5.9a16 16 0 0 0 0-4h3.4a8 8 0 0 1 0 4z"/></svg>
        <span>www.venlowpartners.example</span>
      </li>
    </ul>
  </div>
</body>
</html>
```